Business Card Design Project

Velvet Harbor is a Boutique Clothing. On the business cards I would like to have this included
Website: www.velvetharbor-example.com
Email: shop@velvetharbor-example.com
Owner: Mai Torres & Bo Rinaldi

Industry/Entity Type

Business

Contact Information for Business Card

I wanted something simple and elegant. I have attach business logo.

```html
<!DOCTYPE html>
<html lang="en">
<head>
<meta charset="UTF-8">
<title>Velvet Harbor – Business Card</title>
<link href="https://fonts.googleapis.com/css2?family=Lato:wght@400;700&display=swap" rel="stylesheet">
<style>
  :root {
    --page-bg: #e9e7e5;
    --card-bg: #333333;
    --ink: #ffffff;
    --ink-soft: #e4e4e4;
  }
  * { margin: 0; padding: 0; box-sizing: border-box; }
  html, body {
    width: 1200px;
    height: 900px;
    overflow: hidden;
    background: var(--page-bg);
    font-family: "Lato", Arial, sans-serif;
  }
  .card {
    position: absolute;
    left: 160px;
    top: 178px;
    width: 880px;
    height: 544px;
    background: var(--card-bg);
    border-radius: 272px 0 0 272px;
    color: var(--ink);
  }
  .brand-mark {
    position: absolute;
    left: 79px;
    top: 124px;
    width: 296px;
    height: 296px;
    border: 2px solid var(--ink);
    border-radius: 50%;
    display: flex;
    align-items: center;
    justify-content: center;
  }
  .brand-name {
    font-weight: 400;
    font-size: 34px;
    letter-spacing: 2px;
    color: var(--ink);
    text-align: center;
    line-height: 1.2;
  }
  .owners {
    position: absolute;
    left: 440px;
    top: 166px;
  }
  .owner-names {
    font-weight: 700;
    font-size: 27px;
    letter-spacing: 0.3px;
    color: var(--ink);
  }
  .owner-role {
    font-weight: 400;
    font-size: 19px;
    letter-spacing: 0.5px;
    color: var(--ink-soft);
    margin-top: 2px;
  }
  .contacts {
    position: absolute;
    left: 440px;
    top: 262px;
    list-style: none;
  }
  .contact-item {
    display: flex;
    align-items: center;
    gap: 8px;
    font-family: Arial, "Lato", sans-serif;
    font-size: 23px;
    line-height: 32px;
    color: var(--ink);
  }
  .contact-icon {
    width: 18px;
    height: 18px;
    flex: none;
  }
</style>
</head>
<body>
  <div class="card">
    <div class="brand-mark">
      <span class="brand-name">VELVET<br>HARBOR</span>
    </div>

    <div class="owners">
      <div class="owner-names">MAI TORRES &amp; BO RINALDI</div>
      <div class="owner-role">OWNER</div>
    </div>

    <ul class="contacts">
      <li class="contact-item">
        <svg class="contact-icon" viewBox="0 0 20 20" aria-hidden="true">
          <path d="M2 6c0-2 3-3 8-3s8 1 8 3v1.5h-4V6H6v1.5H2z" fill="#fff"/>
          <path d="M5 9h10l2 7H3z" fill="#fff"/>
          <circle cx="10" cy="12.5" r="1.8" fill="#333"/>
        </svg>
        <span>555 014 2273</span>
      </li>
      <li class="contact-item">
        <svg class="contact-icon" viewBox="0 0 20 20" aria-hidden="true">
          <rect x="2" y="4" width="16" height="12" fill="#fff"/>
          <path d="M2.5 4.5 10 11l7.5-6.5" fill="none" stroke="#333" stroke-width="1.5"/>
        </svg>
        <span>shop@velvetharbor-example.com</span>
      </li>
      <li class="contact-item">
        <svg class="contact-icon" viewBox="0 0 20 20" aria-hidden="true">
          <circle cx="10" cy="10" r="8" fill="#fff"/>
          <path d="M6 5c2 1 2 3 1 4s1 3 3 3-1 4 1 5M12 3c0 2 2 3 4 3" fill="none" stroke="#333" stroke-width="1.5"/>
        </svg>
        <span>www.velvetharbor-example.com</span>
      </li>
    </ul>
  </div>
</body>
</html>
```